Business card for Chiropractic clinics needs reworked / redesigned

The business card in attachment was designed 10 years ago. It is in need of an update.
We have 2 clinics:
VELDHOVE KLINIEK & VELDHOVE KLINIEK NOORD
Only one address needs to be on the card for doctors that only work in one clinic and two addresses need to be on the card for the doctors that work in both clinics.

Target Market(s)

patients/referrers

Industry/Entity Type

Medical

Contact Information for Business Card

Logo (in full or zoomed-in)
Clinic Name
Doctor name and title
clinic address, website, tel, email

Font styles to use
Sans Serif

Colors

Designer to choose colors to be used in the design.

Requirements
Must have
• Good contrast/readability
• We like modern minimalistic designs
• The Bcard needs to project our very high standard of proficiency/professionalism
Should not have
• Not curly
• Not to much colours

```html
<!DOCTYPE html>
<html lang="en">
<head>
<meta charset="utf-8">
<title>Veldhove Kliniek – business card</title>
<link rel="stylesheet" href="https://fonts.googleapis.com/css2?family=Oswald:wght@300;400&family=Poiret+One&display=swap">
<style>
  :root {
    --stage: #000000;
    --paper: #ffffff;
    --band: #80bf93;
    --forest: #1b5a2d;
    --ink-dark: #1b5e2e;
    --ink-mid: #2e7d3f;
    --label-soft: #4f9a65;
    --spine-light: #c9ddd0;
    --spine-dark: #14482a;
  }
  * { margin: 0; padding: 0; box-sizing: border-box; }
  html, body { width: 1200px; height: 1200px; overflow: hidden; background: var(--stage); }
  .canvas { position: relative; width: 1200px; height: 1200px; }

  .side-label {
    position: absolute;
    display: flex; flex-direction: column; align-items: center;
    font-family: "Poiret One", sans-serif;
    font-size: 62px; line-height: 64px;
    color: var(--paper);
  }
  .side-label--back { left: 20px; top: 176px; }
  .side-label--front { left: 1118px; top: 708px; }

  .card { position: absolute; overflow: hidden; }
  .card--back { left: 86px; top: 2px; width: 1000px; height: 592px; background: var(--paper); }
  .card--front { left: 86px; top: 594px; width: 1004px; height: 604px; background: var(--forest); }

  .card__band { position: absolute; left: 0; top: 26px; width: 100%; height: 146px; background: var(--band); }

  .spine-art { position: absolute; }
  .card--back .spine-art { left: 20px; top: 26px; width: 300px; height: 566px; }
  .card--front .spine-art { left: 70px; top: 0; width: 300px; height: 604px; }

  .doctor { position: absolute; right: 22px; top: 56px; text-align: right; }
  .doctor__name {
    font-family: "Poiret One", sans-serif;
    font-size: 60px; line-height: 1; color: var(--ink-dark);
    letter-spacing: 1px;
  }
  .doctor__title {
    position: absolute; left: 0; right: 0; top: 60px; padding-right: 40px;
    text-align: center;
    font-family: "Oswald", sans-serif; font-weight: 400;
    font-size: 28px; line-height: 1; letter-spacing: 17px;
    color: var(--paper);
  }

  .clinic { position: absolute; top: 374px; }
  .clinic--main { left: 58px; }
  .clinic--north { left: 534px; }
  .clinic__name {
    font-family: "Poiret One", sans-serif;
    font-size: 34px; line-height: 42px; white-space: nowrap;
  }
  .clinic--main .clinic__name { color: var(--ink-dark); }
  .clinic--north .clinic__name { color: var(--ink-mid); }
  .clinic__details {
    font-family: "Oswald", sans-serif; font-weight: 400;
    font-size: 29px; line-height: 30px; letter-spacing: -0.6px;
    color: var(--ink-dark); font-style: normal;
    transform: scaleX(0.82); transform-origin: left;
  }

  .brand { position: absolute; left: 0; right: 0; top: 248px; text-align: center; }
  .brand__name {
    font-family: "Poiret One", sans-serif;
    font-size: 100px; line-height: 1; letter-spacing: 2px;
    color: var(--paper);
  }
  .brand__locations {
    position: relative; height: 40px; margin-top: 10px;
    font-family: "Oswald", sans-serif; font-weight: 300;
    font-size: 34px; letter-spacing: 18px; color: var(--label-soft);
  }
  .brand__location { position: absolute; top: 0; transform: translateX(-50%); }
  .brand__location--main { left: 350px; }
  .brand__location--north { left: 668px; }
</style>
</head>
<body>
<main class="canvas">
  <div class="side-label side-label--back" aria-label="Back"><span>B</span><span>A</span><span>C</span><span>K</span></div>
  <div class="side-label side-label--front" aria-label="Front"><span>F</span><span>R</span><span>O</span><span>N</span><span>T</span></div>

  <section class="card card--back">
    <div class="card__band"></div>
    <svg class="spine-art" viewBox="0 0 300 566" role="img" aria-label="Faint illustration of a human spine curving down the left side of the card">
      <defs>
        <linearGradient id="spineBackFill" x1="0" y1="0" x2="0" y2="1">
          <stop offset="0" stop-color="#6aa980" stop-opacity="0.55"/>
          <stop offset="1" stop-color="var(--spine-light)" stop-opacity="0.9"/>
        </linearGradient>
      </defs>
      <rect x="0" y="0" width="300" height="566" rx="40" fill="url(#spineBackFill)" opacity="0.55"/>
    </svg>

    <header class="doctor">
      <h1 class="doctor__name">MAARTEN VERSCHAEVE</h1>
      <p class="doctor__title">CHIROPRACTOR</p>
    </header>

    <div class="clinic clinic--main">
      <h2 class="clinic__name">VELDHOVE KLINIEK</h2>
      <address class="clinic__details">LINDENLAAN 148<br>09 412 58 30<br>VELDHOVEKLINIEK.BE</address>
    </div>
    <div class="clinic clinic--north">
      <h2 class="clinic__name">VELDHOVE KLINIEK NOORD</h2>
      <address class="clinic__details">MOLENSTRAAT 27<br>09 318 46 72<br>VELDHOVENOORD.BE</address>
    </div>
  </section>

  <section class="card card--front">
    <svg class="spine-art" viewBox="0 0 300 604" role="img" aria-label="Dark green illustration of a human spine running down the card">
      <defs>
        <linearGradient id="spineFrontFill" x1="0" y1="0" x2="0" y2="1">
          <stop offset="0" stop-color="#1f6633"/>
          <stop offset="1" stop-color="var(--spine-dark)"/>
        </linearGradient>
      </defs>
      <rect x="0" y="0" width="300" height="604" rx="40" fill="url(#spineFrontFill)" opacity="0.7"/>
    </svg>

    <div class="brand">
      <p class="brand__name">VELDHOVE</p>
      <p class="brand__locations">
        <span class="brand__location brand__location--main">KLINIEK</span>
        <span class="brand__location brand__location--north">NOORD</span>
      </p>
    </div>
  </section>
</main>
</body>
</html>
```